2016 QMB Tournament Trail Schedule

I need a flyer designed for our 2016 QMB Trail. We are a Texas based bass tournament trail. We are announcing $10K guaranteed for first at all 6 regular season events and $20K guaranteed for first at our 2 day fall championship. On the flyer we'd also like to show our schedule.

Jan 30 - Lake LBJ
Feb 27 - Canyon Lake
April 2 - Lake Travis
April 30 - Belton Lake
May 21 - Lake Buchanan
June 18 - Lake Waco

Fall Championship - TBD

Adult teams $200 entry includes big bass pot
Youth/adult teams $150 entry includes big bass pot

The flyer needs to be bass fishing related and we can provide pictures if you have ideas. We do not want it to look redneck'ish though. Our website is qmb1.net and would prefer a similar look. Lot's of black, red, and grey.

We have attached the QMB logo and we would also like Norvane and Dolkira logos incorporated. Norvane boats (which are are owned by Dolkira motors) is our title sponsor

Target Market(s)

Our anglers

Font styles to use
Other font styles liked:
• Something Cool

Colors
474747
ec1f27
000000
dbdbdb

Requirements
Must have
• Tournament dates and locations entry costs, payout guarantees
• QMB logo, Norvane Logo, Dolkira Logo
Nice to have
• go to www.qmb1.net to see our website, this should give you a feel for our style
• or qmbforum.net another site we operate

```html
<!DOCTYPE html>
<html lang="en">
<head>
<meta charset="utf-8">
<title>QMB Tournament Trail Schedule 2016</title>
<link href="https://fonts.googleapis.com/css2?family=Oswald:wght@400;500;600;700&display=swap" rel="stylesheet">
<style>
  :root {
    --red: #ec1f27;
    --red-dark: #b3131a;
    --black: #000000;
    --charcoal: #474747;
    --grey-light: #dbdbdb;
    --white: #ffffff;
    --sunset-hi: #f4a63a;
    --sunset-lo: #a8521a;
  }
  * { margin: 0; padding: 0; box-sizing: border-box; }
  html, body { width: 900px; height: 1200px; overflow: hidden; background: #eeeeee; }
  body { font-family: "Oswald", "Arial Narrow", sans-serif; }

  .flyer {
    position: absolute; left: 0; top: 0; width: 900px; height: 1200px;
    background: var(--grey-light);
    padding: 26px;
  }
  .flyer-inner {
    position: relative; width: 100%; height: 100%;
    background: var(--black); overflow: hidden;
  }

  .title-band {
    height: 118px;
    background: linear-gradient(var(--red-dark) 0 14px, var(--red) 14px 100%);
    display: flex; align-items: center; justify-content: center;
    box-shadow: 0 6px 10px rgba(0,0,0,.5);
    position: relative; z-index: 2;
  }
  .title-band h1 {
    color: var(--white); font-weight: 700; font-size: 50px;
    letter-spacing: 1.5px; text-transform: uppercase;
    text-shadow: 0 3px 4px rgba(0,0,0,.45);
  }

  .feature {
    display: flex; height: 500px;
    background: linear-gradient(180deg, #2b2b2b, #0d0d0d);
  }
  .feature-photo {
    position: relative; width: 52%; height: 100%;
    background: linear-gradient(160deg, var(--sunset-hi) 0%, #d9782a 45%, var(--sunset-lo) 78%, #3a1d0c 100%);
  }
  .client-mark {
    position: absolute; left: 26px; bottom: 28px;
    display: flex; align-items: center; gap: 10px;
  }
  .client-mark .mark-square { width: 26px; height: 26px; background: var(--white); }
  .client-mark span { color: var(--white); font-weight: 700; font-size: 44px; letter-spacing: 2px; }

  .schedule {
    flex: 1; list-style: none; padding: 34px 34px 0 38px;
  }
  .schedule li {
    display: flex; align-items: center; gap: 18px;
    height: 72px; color: var(--white);
    font-size: 27px; font-weight: 500; letter-spacing: 1px; text-transform: uppercase;
    border-bottom: 1px solid rgba(255,255,255,.14);
  }
  .schedule li:last-child { border-bottom: none; }
  .schedule .dot { width: 11px; height: 11px; border-radius: 50%; background: var(--red); flex: none; }

  .prize-band {
    height: 170px; background: var(--black);
    display: flex; align-items: center; justify-content: center; gap: 30px;
    border-top: 3px solid var(--charcoal);
  }
  .prize-amount { color: var(--red); font-weight: 700; font-size: 128px; line-height: 1; }
  .prize-label {
    color: var(--white); font-weight: 600; font-size: 42px; line-height: 1.05;
    letter-spacing: 9px; text-transform: uppercase;
  }

  .entry-band {
    height: 124px; background: var(--red);
    display: flex; flex-direction: column; justify-content: center;
    padding: 0 44px; gap: 4px;
  }
  .entry-band p {
    color: var(--white); font-weight: 600; font-size: 29px;
    text-transform: uppercase; letter-spacing: .5px;
  }

  .footer {
    height: 236px;
    background: linear-gradient(180deg, var(--charcoal), #1e1e1e);
    display: flex; align-items: center; justify-content: space-between;
    padding: 0 44px;
  }
  .footer .site { color: var(--red); font-weight: 700; font-size: 52px; letter-spacing: 1px; }
  .sponsors { display: flex; flex-direction: column; align-items: flex-end; gap: 20px; }
  .sponsor { display: flex; align-items: center; gap: 10px; }
  .sponsor .mark-square { width: 18px; height: 18px; background: var(--white); }
  .sponsor span { color: var(--white); font-weight: 700; font-size: 30px; letter-spacing: 3px; text-transform: uppercase; }
</style>
</head>
<body>
<div class="flyer">
  <div class="flyer-inner">
    <header class="title-band">
      <h1>QMB Tournament Trail Schedule 2016</h1>
    </header>

    <section class="feature">
      <div class="feature-photo" role="img" aria-label="Silhouette of an angler casting from a boat against an orange sunset over a lake">
        <div class="client-mark">
          <div class="mark-square"></div>
          <span>QMB</span>
        </div>
      </div>
      <ul class="schedule">
        <li><span class="dot"></span>Jan 30 - Lake LBJ</li>
        <li><span class="dot"></span>Feb 27 - Canyon Lake</li>
        <li><span class="dot"></span>April 2 - Lake Travis</li>
        <li><span class="dot"></span>April 30 - Belton Lake</li>
        <li><span class="dot"></span>May 21 - Lake Buchanan</li>
        <li><span class="dot"></span>June 18 - Lake Waco</li>
      </ul>
    </section>

    <section class="prize-band">
      <div class="prize-amount">$10K</div>
      <div class="prize-label">Guaranteed<br>for first</div>
    </section>

    <section class="entry-band">
      <p>Adult teams $200 entry includes big bass pot</p>
      <p>Youth/adult teams $150 entry includes big bass pot</p>
    </section>

    <footer class="footer">
      <div class="site">WWW.qmb1.net</div>
      <div class="sponsors">
        <div class="sponsor"><div class="mark-square"></div><span>Norvane</span></div>
        <div class="sponsor"><div class="mark-square"></div><span>Dolkira</span></div>
      </div>
    </footer>
  </div>
</div>
</body>
</html>
```